DRU online New Year's greeting card**

We would like to send an original digital New year's card via Email to all our customers. We are a company located in Belgium (Europe). We load and unload new cars from Roll-on-Roll-off vessels. More info can be found on our website: www.druterminals-example.com

```html
<!DOCTYPE html>
<html lang="en">
<head>
<meta charset="utf-8">
<title>DRU – Happy New Year 2021</title>
<link rel="stylesheet" href="https://fonts.googleapis.com/css2?family=Playfair+Display:wght@900&family=Saira:wght@400&family=Source+Sans+3:wght@400;700&display=swap">
<style>
  :root {
    --navy: #00527f;
    --bright-blue: #00aeef;
    --sky-blue: #6dcff6;
    --pale-blue: #c8e9fa;
    --grey-text: #58595b;
    --ink: #231f20;
    --card-edge: #a7a9ac;
    --paper: #ffffff;
    --paper-shade: #dcdcdf;
  }
  html, body {
    margin: 0;
    padding: 0;
    width: 1200px;
    height: 900px;
    overflow: hidden;
    background: var(--paper);
  }
  .greeting-card { display: block; width: 1200px; height: 900px; }
  .card-edge { stroke: var(--card-edge); stroke-width: 2; }
  .year-figure {
    font-family: "Playfair Display", Georgia, serif;
    font-weight: 900;
    font-size: 800px;
    fill: var(--navy);
  }
  .greeting-line {
    font-family: "Saira", "Arial Narrow", sans-serif;
    font-weight: 400;
    fill: var(--grey-text);
  }
  .contact-line {
    font-family: "Source Sans 3", Arial, sans-serif;
    font-weight: 400;
    font-size: 22px;
    fill: var(--ink);
  }
  .brand-name {
    font-family: "Source Sans 3", Arial, sans-serif;
    font-weight: 700;
    font-size: 78px;
    fill: var(--navy);
  }
  .stroke-navy { stroke: var(--navy); }
  .stroke-bright { stroke: var(--bright-blue); }
  .stroke-sky { stroke: var(--sky-blue); }
  .fill-bright { fill: var(--bright-blue); }
  .fill-sky { fill: var(--sky-blue); }
  .fill-pale { fill: var(--pale-blue); }
  .fill-navy { fill: var(--navy); }
</style>
</head>
<body>
<svg class="greeting-card" viewBox="0 0 2212 1659" xmlns="http://www.w3.org/2000/svg">
  <defs>
    <radialGradient id="paper-glow" cx="50%" cy="50%" r="75%">
      <stop offset="0.45" stop-color="var(--paper)"/>
      <stop offset="1" stop-color="var(--paper-shade)"/>
    </radialGradient>
  </defs>

  <!-- card surface -->
  <rect class="card-edge" x="113" y="120" width="1987" height="1418" fill="url(#paper-glow)"/>

  <!-- back accent strokes -->
  <g class="accent-strokes-back" fill="none">
    <line class="stroke-sky" x1="1680" y1="420" x2="1460" y2="720" stroke-width="4"/>
    <line class="stroke-sky" x1="1180" y1="770" x2="943" y2="1092" stroke-width="4"/>
    <line class="stroke-sky" x1="800" y1="748" x2="612" y2="1004" stroke-width="4"/>
  </g>
  <polygon class="fill-pale" points="1160,930 1188,930 1112,1045 1070,1045"/>

  <!-- year -->
  <text class="year-figure" x="500" y="950" textLength="990" lengthAdjust="spacingAndGlyphs">2021</text>

  <!-- front accent strokes -->
  <g class="accent-strokes-front" fill="none">
    <line class="stroke-navy" x1="720" y1="452" x2="475" y2="779" stroke-width="6"/>
    <line class="stroke-navy" x1="1714" y1="528" x2="1345" y2="1024" stroke-width="6"/>
    <line class="stroke-bright" x1="1362" y1="288" x2="703" y2="1180" stroke-width="20"/>
  </g>
  <polygon class="fill-pale" points="758,692 782,692 676,838 651,838"/>
  <polygon class="fill-bright" points="999,508 1022,508 968,580 946,580"/>
  <polygon class="fill-sky" points="1066,583 1081,583 982,713 965,713"/>
  <polygon class="fill-sky" points="1412,849 1434,849 1346,969 1326,969"/>

  <!-- greeting -->
  <text class="greeting-line" x="1735" y="789" font-size="62" text-anchor="end" textLength="162" lengthAdjust="spacingAndGlyphs">HAPPY</text>
  <text class="greeting-line" x="1735" y="866" font-size="92" text-anchor="end" textLength="192" lengthAdjust="spacingAndGlyphs">NEW</text>
  <text class="greeting-line" x="1735" y="950" font-size="100" text-anchor="end" textLength="258" lengthAdjust="spacingAndGlyphs">YEAR</text>

  <!-- contact block -->
  <g class="contact-block">
    <text class="contact-line" x="184" y="1360">Havenstad office</text>
    <text class="contact-line" x="184" y="1386">Havenkaai 12</text>
    <text class="contact-line" x="184" y="1412">0000 Havenstad, Belgium</text>
    <text class="contact-line" x="184" y="1438">Tel. +32 (0)00 12 34 56</text>
    <text class="contact-line" x="184" y="1464">info@druterminals-example.com</text>
  </g>

  <!-- brand name -->
  <text class="brand-name" x="1865" y="1426" text-anchor="middle">DRU</text>

  <!-- footer bands -->
  <polygon class="fill-bright" points="113,1493 1406,1493 1349,1538 113,1538"/>
  <polygon class="fill-navy" points="1444,1493 2100,1493 2100,1538 1387,1538"/>
</svg>
</body>
</html>
```